Kitchen and bathroom exhaust fan cleaning business card design

A new business cleaning domestic - not commercial - exhaust/extractor fans in kitchens, bathrooms and en suites and kitchen range hood filters.

We would like a bright colour suggesting cleanliness (such a syellow or light green?)

I would like to see on the card preferably on the reverse:

"We clean kitchen and bathroom exhaust fans & Vormo Heatlites
and
clean and repair range hood filters and replace carbon filters

We give Pensioner discounts

Designers pls note the TM in the contact filed after Brisko Airworks should be superscript as in the trademark sign. On the reverse of the card, I would like:: "We clean kitchen and bathroom exhaust fans & Vormo Heatlites & clean and repair range hood filters and replace carbon filters We give Pensioner discounts

Reason: I will be out of the country for several days

Target Market(s)

people who are too lazy or too busy to clean their fan units and pensioners and others who are unable to do it.

Industry/Entity Type

Business

Contact Information for Business Card

Brisko AirworksTM Designer pls note the TM should be superscript as in the trademark sign
Alan Petworth
Mob: 0491 570 263
Email: briskoairworks@postlume.net
PO Box 7152, Larkford QLD 4891

Requirements
Must have
• Designer pls note the TM in the contact filed after Brisko Airworks should be superscript as in the trademark sign.

On the reverse

and

```html
<!DOCTYPE html>
<html lang="en">
<head>
<meta charset="utf-8">
<title>Brisko Airworks – Business Card</title>
<link rel="stylesheet" href="https://fonts.googleapis.com/css2?family=Titillium+Web:wght@400;700&display=swap">
<style>
  :root {
    --page-bg: #e6e8e6;
    --front-green: #5cbb46;
    --back-green-top: #3aaa4a;
    --back-green-bottom: #8fc540;
    --accent-yellow: #f2e21c;
    --grille-light: #d9dbdc;
    --grille-dark: #6f7375;
    --text-white: #ffffff;
    --card-shadow: 0 10px 30px rgba(0,0,0,0.18);
  }
  * { margin: 0; padding: 0; box-sizing: border-box; }
  html, body {
    width: 1200px; height: 900px; overflow: hidden;
    background: var(--page-bg);
    font-family: "Titillium Web", sans-serif;
    color: var(--text-white);
  }
  .canvas {
    width: 1200px; height: 900px;
    display: flex; align-items: center; justify-content: center; gap: 40px;
  }
  .card {
    position: relative;
    width: 540px; height: 309px;
    border-radius: 4px;
    overflow: hidden;
    box-shadow: var(--card-shadow);
  }
  /* Front */
  .card--front {
    background: var(--front-green);
    display: flex; align-items: center; justify-content: center;
  }
  .brand { text-align: center; line-height: 1; }
  .brand__name {
    font-weight: 700; font-size: 40px; letter-spacing: 0.5px;
  }
  .brand__name sup { font-size: 0.4em; vertical-align: super; }
  .brand__person {
    display: block; margin-top: 4px;
    font-weight: 400; font-size: 17px;
  }
  /* Back */
  .card__art { position: absolute; inset: 0; width: 100%; height: 100%; }
  .back-brand {
    position: absolute; right: 28px; top: 36px; text-align: center;
  }
  .back-brand .brand__name { font-size: 30px; }
  .back-brand .brand__person { font-size: 15px; margin-top: 3px; }
  .contact-list {
    position: absolute; left: 250px; top: 174px;
    list-style: none;
    font-size: 15px; line-height: 1.25;
  }
  .contact-list li {
    display: flex; align-items: center; gap: 10px; margin-bottom: 8px;
  }
  .contact-list svg { width: 14px; height: 14px; flex: none; }
</style>
</head>
<body>
<main class="canvas">

  <section class="card card--front" aria-label="Card front">
    <div class="brand">
      <div class="brand__name">Brisko Airworks<sup>TM</sup></div>
      <span class="brand__person">Alan Petworth</span>
    </div>
  </section>

  <section class="card card--back" aria-label="Card back">
    <svg class="card__art" viewBox="0 0 540 309" preserveAspectRatio="none">
      <defs>
        <linearGradient id="backGreen" x1="0" y1="0" x2="0" y2="1">
          <stop offset="0" stop-color="var(--back-green-top)"/>
          <stop offset="1" stop-color="var(--back-green-bottom)"/>
        </linearGradient>
        <linearGradient id="grilleTone" x1="0" y1="0" x2="1" y2="1">
          <stop offset="0" stop-color="var(--grille-dark)"/>
          <stop offset="0.5" stop-color="var(--grille-light)"/>
          <stop offset="1" stop-color="var(--grille-dark)"/>
        </linearGradient>
      </defs>
      <rect width="540" height="309" fill="url(#backGreen)"/>
      <path d="M0 0 H300 C270 130 200 250 90 309 H0 Z" fill="url(#grilleTone)"
            role="img" aria-label="Photo of a clean metal exhaust fan grille"/>
      <path d="M300 0 C270 130 200 250 90 309" fill="none"
            stroke="var(--accent-yellow)" stroke-width="4"/>
    </svg>

    <div class="back-brand">
      <div class="brand__name">Brisko Airworks<sup>TM</sup></div>
      <span class="brand__person">Alan Petworth</span>
    </div>

    <ul class="contact-list">
      <li>
        <svg viewBox="0 0 14 14"><path d="M7 1a4 4 0 0 1 4 4c0 3-4 8-4 8S3 8 3 5a4 4 0 0 1 4-4z" fill="#fff"/><circle cx="7" cy="5" r="1.5" fill="var(--back-green-top)"/></svg>
        PO Box 7152, Larkford QLD 4891
      </li>
      <li>
        <svg viewBox="0 0 14 14"><rect x="1" y="3" width="12" height="8" fill="#fff"/><path d="M1 3l6 5 6-5" fill="none" stroke="var(--back-green-top)" stroke-width="1"/></svg>
        briskoairworks@postlume.net
      </li>
      <li>
        <svg viewBox="0 0 14 14"><rect x="4" y="1" width="6" height="12" rx="1" fill="none" stroke="#fff" stroke-width="1.3"/><line x1="6" y1="11" x2="8" y2="11" stroke="#fff"/></svg>
        0491 570 263
      </li>
    </ul>
  </section>

</main>
</body>
</html>
```